VELORA Group Fitness Class Launch Poster!

We need a poster design for a upcoming Group Fitness Class launch with two additional social media post designs.
Please follow our Brand Style Guide, as I will not be able to accept anything outside of this guide.
Class Description:
Come and VELORA your body with this class while catching up with friends and meeting new people. It is low-impact strength training with bodyweight exercises to help improve muscular strength, cardiovascular endurance, balance, bone health and functional training. It is suitable for all fitness levels.
Class Length: 30 Minutes
Intro script for class online:
📣New class alert❗
TPW team is excited to announce the launch of our new class, "VELORA", instructed by Jo! 🥰
Unsure if group fitness classes are for you? Join us for 30-minute low-impact strength training with bodyweight exercises! It's time to build your confidence in a fun and supportive environment.
Target Market(s)
Target audience is mostly females which barrier to entry to fitness is not having the confidence to join or has limited capability and needing low impact. Important to note that our demographic tends to be below 50... So barriers is most likely to be confidence, overweight or unfit.
Industry/Entity Type
Fitness
Other font styles liked:
- Please follow the Style Guide Fonts.
Requirements
Must have
- The project must follow our Brand Guidelines & include the class logo. Poster should be exciting and stand out. Don't necessarily have to use the stock images provided.
Should not have
- If you select your own image, the preference would be that it does not only include slim/fit looking individuals.

```html
<!DOCTYPE html>
<html lang="en">
<head>
<meta charset="utf-8">
<title>VELORA Class Launch Poster</title>
<link rel="stylesheet" href="https://fonts.googleapis.com/css2?family=Anton&family=Oswald:wght@600&family=Poppins:wght@400;500;700;800&display=swap">
<style>
  :root {
    --page-bg: #efefef;
    --grey-dark: #5f5f5f;
    --grey-mid: #8e8e8e;
    --grey-light: #b4b4b4;
    --brand-red: #a8172c;
    --ink: #111111;
    --white: #ffffff;
    --muted: #dedede;
    --prop-dark: #2a2a2a;
    --prop-edge: #4a4a4a;
  }
  * { box-sizing: border-box; margin: 0; padding: 0; }
  html, body { width: 1200px; height: 2878px; overflow: hidden; background: var(--page-bg); }
  .poster {
    position: absolute; left: 0; top: 640px;
    width: 991px; height: 1320px;
    transform: scale(1.2109); transform-origin: top left;
    background: linear-gradient(180deg, var(--grey-mid), var(--grey-light));
    overflow: hidden;
    font-family: "Poppins", sans-serif;
  }
  .poster > * { position: absolute; }
  .backdrop { left: 0; top: 0; width: 991px; height: 1320px; }

  .class-title {
    left: 0; width: 991px; top: 66px; text-align: center;
    font-family: "Anton", sans-serif; font-size: 120px; line-height: 1;
    color: var(--white); letter-spacing: 3px;
  }

  .prop {
    border-radius: 18px;
    background: radial-gradient(circle at 35% 30%, var(--prop-edge), var(--prop-dark) 70%);
    box-shadow: 0 4px 8px rgba(0,0,0,.3);
  }
  .kettlebell-lg { left: 22px; top: 28px; width: 106px; height: 126px; }
  .kettlebell-sm { left: 100px; top: 168px; width: 80px; height: 100px; }
  .dumbbell-top { left: 795px; top: 40px; width: 180px; height: 76px; }
  .dumbbell-diag { left: 858px; top: 136px; width: 116px; height: 146px; }
  .dumbbell-left { left: 76px; top: 1056px; width: 104px; height: 90px; }
  .dumbbell-right { left: 810px; top: 1056px; width: 104px; height: 90px; }

  .photo-frame {
    left: 97px; top: 208px; width: 793px; height: 609px;
    background: var(--white);
    border-radius: 46% 44% 48% 50% / 38% 40% 52% 50%;
  }
  .class-photo {
    left: 130px; top: 241px; width: 750px; height: 548px;
    border-radius: 26% 26% 44% 44% / 14% 14% 40% 40%;
    background: linear-gradient(180deg, #54565a 0%, #3f4248 48%, #b3845a 74%, #c29366 100%);
  }

  .megaphone {
    left: 88px; top: 858px; width: 130px; height: 140px; border-radius: 18px;
    background: linear-gradient(135deg, var(--brand-red) 0%, #e9e9e9 75%);
  }
  .alert-banner { left: 225px; top: 869px; width: 590px; height: 112px; }
  .alert-text {
    left: 240px; top: 876px; width: 570px; text-align: center;
    font-family: "Anton", sans-serif; font-size: 78px; line-height: 1.2; color: var(--white);
  }
  .alert-mark { left: 845px; top: 850px; width: 36px; height: 128px; }

  .announce {
    left: 0; width: 991px; top: 1009px; text-align: center;
    font-size: 18.5px; font-weight: 500; color: var(--ink); line-height: 24px;
  }
  .class-name-box {
    left: 293px; top: 1042px; width: 203px; height: 45px;
    border: 3px solid var(--ink); border-bottom-width: 5px;
    font-weight: 800; font-size: 38px; line-height: 37px; text-align: center; color: var(--ink);
  }
  .instructor { left: 293px; top: 1094px; width: 203px; text-align: center; font-size: 20px; line-height: 26px; font-weight: 500; color: var(--muted); }
  .instructor b { color: var(--ink); font-weight: 700; }
  .length-label {
    left: 541px; top: 1040px; font-size: 26px; font-weight: 500; color: var(--brand-red);
    border-bottom: 2px solid var(--ink); line-height: 30px;
  }
  .length-value { left: 541px; top: 1076px; font-size: 48px; line-height: 50px; white-space: nowrap; }
  .length-value .num { font-family: "Oswald", sans-serif; color: var(--ink); }
  .length-value .unit { font-weight: 800; font-size: 38px; color: #e4e4e4; margin-left: 4px; }

  .info-band { left: 0; top: 1132px; width: 991px; height: 158px; }
  .info-text {
    left: 20px; width: 951px; top: 1160px; text-align: center;
    font-size: 14.5px; font-weight: 500; line-height: 17px; color: var(--white);
  }
  .info-text p + p { margin-top: 17px; }
</style>
</head>
<body>
  <main class="poster">
    <svg class="backdrop" viewBox="0 0 991 1320" aria-hidden="true">
      <polygon points="0,0 991,0 991,515 495,730 0,515" fill="var(--grey-dark)"/>
    </svg>

    <div class="prop kettlebell-lg" role="img" aria-label="Black kettlebell"></div>
    <div class="prop kettlebell-sm" role="img" aria-label="Small black kettlebell"></div>
    <div class="prop dumbbell-top" role="img" aria-label="Black dumbbell"></div>
    <div class="prop dumbbell-diag" role="img" aria-label="Black dumbbell, angled"></div>

    <h1 class="class-title">VELORA</h1>

    <div class="photo-frame" aria-hidden="true"></div>
    <div class="class-photo" role="img" aria-label="Instructor and two participants doing squats in a gym"></div>

    <div class="megaphone" role="img" aria-label="Red and white megaphone"></div>
    <svg class="alert-banner" viewBox="0 0 590 112" aria-hidden="true">
      <polygon points="12,0 590,0 582,112 0,112" fill="var(--brand-red)"/>
    </svg>
    <div class="alert-text">NEW CLASS ALERT</div>
    <svg class="alert-mark" viewBox="0 0 36 128" aria-hidden="true">
      <polygon points="2,0 34,0 30,92 6,92" fill="#6a6a6a"/>
      <rect x="5" y="102" width="26" height="26" fill="#6a6a6a"/>
    </svg>

    <p class="announce">TPW TEAM IS EXCITED TO ANNOUNCE THE LAUNCH OF OUR NEW CLASS</p>
    <div class="class-name-box">VELORA</div>
    <p class="instructor">INSTRUCTED BY <b>JO!</b></p>
    <p class="length-label">CLASS LENGTH</p>
    <p class="length-value"><span class="num">30</span><span class="unit">Minutes</span></p>

    <div class="prop dumbbell-left" role="img" aria-label="Pair of black dumbbells"></div>
    <div class="prop dumbbell-right" role="img" aria-label="Pair of black dumbbells"></div>

    <svg class="info-band" viewBox="0 0 991 158" aria-hidden="true">
      <path d="M0,14 L120,6 L300,12 L520,3 L760,10 L991,4 L991,152 L700,158 L420,150 L180,157 L0,151 Z" fill="var(--brand-red)"/>
    </svg>
    <div class="info-text">
      <p>Unsure if group fitness classes are for you? Join us for 30-minute low-impact strength training with bodyweight exercises!<br>It's time to build your confidence in a fun and supportive environment.</p>
      <p>Come and VELORA your body with this class while catching up with friends and meeting new people. It is low-impact<br>strength training with bodyweight exercises to help improve muscular strength, cardiovascular endurance, balance,<br>bone health and functional training. It is suitable for all fitness levels.</p>
    </div>
  </main>
</body>
</html>
```